HVL Regal Business Card Design 2020

Harbor Vale Living is looking for a business card that is clean and straight to the point but still looks high-end and attractive. We are a team comprised of management and field professionals focused on the high-end residential marketplace. We serve homeowners and trade professionals directly based out of the Metrowest/Boston area. We provide client services as well as construction/renovation services.
We are aiming for a black and white feel (white background and black text) and a matte finish with rounded edges.

We want to emphasis our vision of "Properties - Projects - Partners".
Dana Pritchell is the president of HVL

Please include the following areas we service: Boston/Cape/Newport
Please make sure to include Dana's mobile (617) 555 0143 & office number (617) 555 0187, email dana@harborvaleliving.example and website www.harborvaleliving.example

Colors

Designer to choose only greyscale colors for use in the design.

Requirements
Must have
• Include "Properties - Projects - Partners" in design

Include "After Hours Emergency Support # 1800 555 0199" with icon

```html
<!DOCTYPE html>
<html lang="en">
<head>
<meta charset="utf-8">
<title>HVL Business Card</title>
<link rel="stylesheet" href="https://fonts.googleapis.com/css2?family=Lato:wght@400;700&display=swap">
<style>
  :root {
    --page: #2a2a2a;
    --card: #ffffff;
    --card-shadow: rgba(0, 0, 0, 0.45);
    --ink: #111111;
    --ink-soft: #333333;
    --ink-muted: #6e6e6e;
    --rule: #c8c8c8;
    --icon-bg: #1a1a1a;
    --icon-ink: #ffffff;
  }
  * { margin: 0; padding: 0; box-sizing: border-box; }
  html, body {
    width: 1200px; height: 997px; overflow: hidden;
    background: var(--page);
    font-family: "Lato", Arial, sans-serif;
    color: var(--ink);
  }
  .stage {
    width: 1200px; height: 997px;
    display: flex; flex-direction: column;
    align-items: center; justify-content: center; gap: 56px;
  }
  .card {
    width: 700px; height: 400px;
    background: var(--card);
    border-radius: 26px;
    box-shadow: 0 10px 30px var(--card-shadow);
    position: relative;
  }

  /* brand lockup */
  .brand { display: flex; flex-direction: column; align-items: center; color: var(--ink); font-weight: 700; }
  .brand__short { font-size: 92px; line-height: 1; letter-spacing: 2px; }
  .brand__full { font-size: 17px; letter-spacing: 4px; text-transform: uppercase; margin-top: 10px; }

  /* front */
  .card--brand { display: flex; align-items: center; justify-content: center; }

  /* back */
  .card--details { display: flex; flex-direction: column; padding: 36px 48px 28px; }
  .details__main { display: flex; align-items: center; flex: 1; }
  .card--details .brand { width: 230px; flex-shrink: 0; }
  .card--details .brand__short { font-size: 72px; }
  .card--details .brand__full { font-size: 12px; letter-spacing: 3px; }
  .divider {
    width: 2px; height: 170px; margin: 0 30px; flex-shrink: 0;
    background: linear-gradient(to bottom, transparent, var(--ink-muted), transparent);
  }
  .contact { display: flex; flex-direction: column; font-size: 15px; color: var(--ink-soft); }
  .contact__name { font-size: 22px; color: var(--ink); font-weight: 700; }
  .contact__role { font-size: 14px; color: var(--ink-muted); margin: 0 0 10px 2px; }
  .contact__address { line-height: 1.35; margin-bottom: 6px; }
  .contact__line { display: flex; align-items: center; gap: 10px; margin-top: 6px; }
  .icon {
    width: 22px; height: 22px; border-radius: 50%; flex-shrink: 0;
    background: var(--icon-bg);
    display: flex; align-items: center; justify-content: center;
  }
  .icon svg { width: 12px; height: 12px; }

  .details__footer {
    border-top: 1px solid var(--rule);
    padding-top: 12px;
    display: flex; flex-direction: column; align-items: center; gap: 8px;
  }
  .vision { font-size: 16px; letter-spacing: 1px; color: var(--ink); font-weight: 700; }
  .footer__row {
    width: 100%;
    display: flex; justify-content: space-between; align-items: center;
    font-size: 13px; color: var(--ink-soft);
  }
  .service-areas { letter-spacing: 0.5px; }
  .emergency { display: flex; align-items: center; gap: 8px; }
  .emergency .icon { width: 20px; height: 20px; }
</style>
</head>
<body>
<main class="stage">
  <section class="card card--brand">
    <div class="brand">
      <span class="brand__short">HVL</span>
      <span class="brand__full">Harbor Vale Living</span>
    </div>
  </section>

  <section class="card card--details">
    <div class="details__main">
      <div class="brand">
        <span class="brand__short">HVL</span>
        <span class="brand__full">Harbor Vale Living</span>
      </div>
      <div class="divider"></div>
      <div class="contact">
        <span class="contact__name">Dana Pritchell</span>
        <span class="contact__role">President</span>
        <span class="contact__address">48 Linden Crest Rd #2,<br>Ashcombe, MA 01999</span>
        <span class="contact__line">
          <span class="icon"><svg viewBox="0 0 16 16"><rect x="4" y="1" width="8" height="14" rx="1.5" fill="var(--icon-ink)"/><rect x="5.5" y="3" width="5" height="8" fill="var(--icon-bg)"/></svg></span>
          (617) 555 0143
        </span>
        <span class="contact__line">
          <span class="icon"><svg viewBox="0 0 16 16"><path fill="var(--icon-ink)" d="M3 1h3l1.5 4-2 1.2a9 9 0 0 0 4.3 4.3L11 8.5l4 1.5v3a2 2 0 0 1-2 2A13 13 0 0 1 1 3a2 2 0 0 1 2-2z"/></svg></span>
          (617) 555 0187
        </span>
        <span class="contact__line">
          <span class="icon"><svg viewBox="0 0 16 16"><rect x="1" y="3" width="14" height="10" rx="1" fill="var(--icon-ink)"/><path d="M1.5 3.5 8 9l6.5-5.5" fill="none" stroke="var(--icon-bg)" stroke-width="1.3"/></svg></span>
          dana@harborvaleliving.example
        </span>
        <span class="contact__line">
          <span class="icon"><svg viewBox="0 0 16 16"><g fill="none" stroke="var(--icon-ink)" stroke-width="1.4"><circle cx="8" cy="8" r="6.5"/><ellipse cx="8" cy="8" rx="3" ry="6.5"/><path d="M1.5 8h13"/></g></svg></span>
          www.harborvaleliving.example
        </span>
      </div>
    </div>
    <div class="details__footer">
      <p class="vision">Properties - Projects - Partners</p>
      <div class="footer__row">
        <span class="service-areas">Serving Boston / Cape / Newport</span>
        <span class="emergency">
          <span class="icon"><svg viewBox="0 0 16 16"><g fill="none" stroke="var(--icon-ink)" stroke-width="1.6"><circle cx="8" cy="8" r="6.5"/><path d="M8 4v4.5l3 1.8"/></g></svg></span>
          After Hours Emergency Support # 1800 555 0199
        </span>
      </div>
    </div>
  </section>
</main>
</body>
</html>
```